Tidewalk Intro Course QM Dive Bonaire

QM Dive is looking for a great flyer to promote our Tidewalk Intro Course around Bonaire, the Caribbean.

Bonaire is shore dive capital of the world.
Our guests rent a pick-up truck. we would like to inform them about the possibilities of the Tidewalk Intro Dive.

We have the logo, images and text available. Its the catchy and mind blowing design we are looking for to create an eye-catch flyer.
One side will be in English, the other side will be in Dutch.

Target Market(s)

Visitors (non divers) of the island Bonaire

Industry/Entity Type

Diving industry

Font styles to use
Sans Serif

Colors
0094D4
00A9DD
6FCCEA
C7EBF8
E9F6FB
F0912C
F2A743
F7CA91
FBE8D2
FDF5EE

Requirements
Must have
• The picture with the car and divers next to it is mandatory. Inspire to go for a tidewalk intro dive, show the beauty under water, easy to come dive with us, just takes half a day
Should not have
• Should not have pictures taken not around Bonaire.

```html
<!DOCTYPE html>
<html lang="en">
<head>
<meta charset="utf-8">
<title>Tidewalk Intro Course – QM Dive Bonaire</title>
<link href="https://fonts.googleapis.com/css2?family=Poppins:ital,wght@0,400;0,600;0,700;1,500&family=Montserrat:wght@500&family=Kaushan+Script&display=swap" rel="stylesheet">
<style>
  :root{
    --blue-deep:#0094D4;
    --blue:#00A9DD;
    --blue-light:#6FCCEA;
    --blue-pale:#C7EBF8;
    --navy:#1d3f93;
    --orange:#F0912C;
    --orange-bright:#F7A41E;
    --gold:#F2A743;
    --ink:#151515;
    --body:#2b2b2b;
    --plum:#4a1942;
    --red:#e5262a;
    --stage:#b8b8b8;
  }
  *{margin:0;padding:0;box-sizing:border-box}
  html,body{width:1200px;height:873px;overflow:hidden}
  body{background:var(--stage);font-family:"Poppins",sans-serif;position:relative}
  .flyer{position:absolute;left:300px;top:16px;width:599px;height:840px;overflow:hidden;
    background:linear-gradient(160deg,#ffffff 0%,#ececec 55%,#f6f6f6 100%);
    box-shadow:4px 6px 14px rgba(0,0,0,.3)}
  .abs{position:absolute}
  .hero-art{left:0;top:0;width:599px;height:840px}
  .header-line{left:40px;width:330px;top:86px;text-align:center;color:#fff;
    font-family:"Montserrat",sans-serif;font-weight:500;font-size:20px;line-height:24px}
  .headline-script{left:38px;top:134px;font-family:"Kaushan Script",cursive;font-size:92px;line-height:1;
    color:var(--orange-bright);text-shadow:2px 3px 4px rgba(0,0,0,.25)}
  .badge-off{left:139px;top:237px;width:54px;height:54px;border-radius:50%;background:#fff;
    text-align:center;color:var(--red);box-shadow:0 2px 5px rgba(0,0,0,.2);z-index:2}
  .badge-off b{display:block;font-size:17px;font-weight:700;line-height:17px;margin-top:12px}
  .badge-off span{display:block;font-size:9px;line-height:10px}
  .badge-price{left:175px;top:256px;width:102px;height:102px;border-radius:50%;
    background:radial-gradient(circle at 40% 35%,var(--blue-light),var(--blue-deep) 75%);color:#fff;text-align:center}
  .badge-price .from{display:block;font-size:11px;font-weight:600;margin-top:20px;padding-left:18px}
  .badge-price .amount{display:block;font-size:25px;font-weight:700;line-height:26px}
  .badge-price .amount small{font-size:10px;line-height:10px;display:inline-block;vertical-align:top;text-align:left}
  .badge-price s{display:block;font-size:10px;color:var(--blue-pale)}
  .brand{left:400px;top:42px;width:170px;text-align:center;font-size:15px;font-weight:700;color:var(--navy);line-height:18px}
  .polaroid{background:#fff;padding:6px 6px 0;box-shadow:2px 4px 8px rgba(0,0,0,.3)}
  .polaroid .shot{width:100%}
  .polaroid .caption{font-family:"Kaushan Script",cursive;color:var(--orange);text-align:center;font-size:14px;line-height:24px}
  .p-car{left:413px;top:225px;width:137px;z-index:3}
  .p-car .shot{height:106px;background:linear-gradient(180deg,#6fb7de 0%,#9fd2ea 40%,#e8e3d8 60%,#d8d0c2 100%)}
  .p-tanks{left:298px;top:275px;width:168px;transform:rotate(-20deg);z-index:2}
  .p-tanks .shot{height:118px;background:linear-gradient(170deg,#c2dbe6 0%,#8aa4ac 45%,#3b3f44 70%,#e0ddd4 100%)}
  .p-snapper{left:402px;top:400px;width:140px;transform:rotate(20deg);z-index:1}
  .p-snapper .shot{height:108px;background:linear-gradient(160deg,#3a8bc1 0%,#2c6e9a 50%,#7a6f5a 100%)}
  h2{font-weight:700;font-size:18px;line-height:21px;color:var(--ink)}
  h2 em{font-style:normal;color:var(--orange)}
  .lead{border-left:2px solid var(--orange);padding-left:7px;font-size:10px;line-height:13.6px;color:var(--body)}
  .intro{left:38px;top:448px;width:240px}
  .intro .lead{margin-top:6px}
  .passion{left:38px;top:556px;width:262px}
  .checks{list-style:none;margin-top:8px}
  .checks li{display:flex;gap:7px;font-size:8.6px;line-height:10.6px;color:var(--body);height:32px;align-items:flex-start}
  .checks li svg{flex:0 0 14px;margin-top:2px}
  .checks li span{width:214px}
  .paradise{left:326px;top:552px;width:236px}
  .paradise .lead{margin-top:6px;text-align:justify}
  .paradise .lead p+p{margin-top:13px}
  .note{left:326px;top:716px;width:240px;text-align:center;font-size:8px;line-height:10px;font-style:italic;font-weight:500;color:var(--navy)}
  .book-now{left:351px;top:776px;font-weight:700;font-size:17px;line-height:16px;color:var(--plum)}
  .book-icon{left:412px;top:779px}
  .contact{left:451px;top:776px}
  .contact b{display:block;font-size:18px;font-weight:700;color:var(--ink);line-height:20px}
  .contact span{display:block;font-size:8.5px;color:var(--plum)}
</style>
</head>
<body>
<main class="flyer">
  <svg class="abs hero-art" viewBox="0 0 599 840">
    <defs>
      <linearGradient id="sea" x1="0" y1="0" x2="0.6" y2="1">
        <stop offset="0" stop-color="#1a8fb4"/>
        <stop offset="0.35" stop-color="#2aa6c6"/>
        <stop offset="0.6" stop-color="#c49a5c"/>
        <stop offset="1" stop-color="#e0c493"/>
      </linearGradient>
    </defs>
    <path role="img" aria-label="Underwater photo of a Bonaire reef with coral and a Christmas tree worm"
      fill="url(#sea)"
      d="M0,0 H372 C420,40 470,110 470,210 L470,300 C420,320 360,330 300,340 C260,300 220,300 190,320 C150,350 120,400 80,430 C50,450 20,455 0,458 Z"/>
    <path d="M0,458 C20,455 50,450 80,430 C120,400 150,350 190,320 C170,360 140,420 100,450 C60,478 20,480 0,482 Z" fill="var(--blue-deep)"/>
    <path d="M362,0 C420,40 470,110 470,210 L470,300 L478,300 L478,210 C478,110 440,40 386,0 Z" fill="var(--navy)"/>
    <path d="M372,0 H599 V90 C560,90 520,110 470,120 C420,120 385,100 380,60 C378,30 375,12 372,0 Z" fill="#fff"/>
    <path d="M599,70 C560,76 520,104 470,118 L478,126 C520,112 560,92 599,90 Z" fill="var(--blue-deep)"/>
    <path d="M272,840 C300,800 340,780 400,770 C470,758 540,756 599,756 V772 C540,770 480,774 420,784 C370,792 340,812 320,840 Z" fill="var(--blue-deep)"/>
    <path d="M320,840 C340,812 370,792 420,784 C480,774 540,770 599,772 V840 Z" fill="#fff"/>
  </svg>

  <p class="abs header-line">Tidewalk Intro Course<br>on the</p>
  <p class="abs headline-script">Bonaire</p>

  <div class="abs badge-off"><b>30%</b><span>OFF</span></div>
  <div class="abs badge-price">
    <span class="from">Price From</span>
    <span class="amount">$7.5 <small>k<br>Only</small></span>
    <s>was $99k</s>
  </div>

  <p class="abs brand">QM Dive Bonaire</p>

  <figure class="abs polaroid p-tanks">
    <div class="shot" role="img" aria-label="Dive tanks and gear resting on rocks by the shore"></div>
    <figcaption class="caption">Tanks</figcaption>
  </figure>
  <figure class="abs polaroid p-snapper">
    <div class="shot" role="img" aria-label="School of snapper swimming over the reef"></div>
    <figcaption class="caption">Snapper</figcaption>
  </figure>
  <figure class="abs polaroid p-car">
    <div class="shot" role="img" aria-label="Two divers in gear standing next to a white pick-up truck on the beach"></div>
    <figcaption class="caption">QM Dive Promo</figcaption>
  </figure>

  <section class="abs intro">
    <h2>Tidewalk Intro Course<br>on <em>Bonaire</em></h2>
    <p class="lead">Fall in love with diving in our underwater paradise. Under the guidance of a dive instructor you will learn the basic skills for peaceful diving in a fun and easy way.</p>
  </section>

  <section class="abs passion">
    <h2>Develop a Passion for<br><em>Marine Life</em></h2>
    <ul class="checks">
      <li><svg width="14" height="14" viewBox="0 0 14 14"><circle cx="7" cy="7" r="6" fill="none" stroke="var(--orange)" stroke-width="1.3"/><path d="M4.2 7.2l2 2 3.6-4" fill="none" stroke="var(--orange)" stroke-width="1.3"/></svg><span>Ages 10 and up can sign up for our tidewalk intro dive.</span></li>
      <li><svg width="14" height="14" viewBox="0 0 14 14"><circle cx="7" cy="7" r="6" fill="none" stroke="var(--orange)" stroke-width="1.3"/><path d="M4.2 7.2l2 2 3.6-4" fill="none" stroke="var(--orange)" stroke-width="1.3"/></svg><span>You'll dive straight into the water after a brief theoretic introduction.</span></li>
      <li><svg width="14" height="14" viewBox="0 0 14 14"><circle cx="7" cy="7" r="6" fill="none" stroke="var(--orange)" stroke-width="1.3"/><path d="M4.2 7.2l2 2 3.6-4" fill="none" stroke="var(--orange)" stroke-width="1.3"/></svg><span>The Tidewalk Intro Course will take 3-4 hours.</span></li>
      <li><svg width="14" height="14" viewBox="0 0 14 14"><circle cx="7" cy="7" r="6" fill="none" stroke="var(--orange)" stroke-width="1.3"/><path d="M4.2 7.2l2 2 3.6-4" fill="none" stroke="var(--orange)" stroke-width="1.3"/></svg><span>Before participating, you are required to fill out a medical questionnaire.</span></li>
      <li><svg width="14" height="14" viewBox="0 0 14 14"><circle cx="7" cy="7" r="6" fill="none" stroke="var(--orange)" stroke-width="1.3"/><path d="M4.2 7.2l2 2 3.6-4" fill="none" stroke="var(--orange)" stroke-width="1.3"/></svg><span>A group consists of a maximum of 4 people.</span></li>
      <li><svg width="14" height="14" viewBox="0 0 14 14"><circle cx="7" cy="7" r="6" fill="none" stroke="var(--orange)" stroke-width="1.3"/><path d="M4.2 7.2l2 2 3.6-4" fill="none" stroke="var(--orange)" stroke-width="1.3"/></svg><span>Experience the splendor of the ocean without much distraction by other divers.</span></li>
      <li><svg width="14" height="14" viewBox="0 0 14 14"><circle cx="7" cy="7" r="6" fill="none" stroke="var(--orange)" stroke-width="1.3"/><path d="M4.2 7.2l2 2 3.6-4" fill="none" stroke="var(--orange)" stroke-width="1.3"/></svg><span>And enjoy a lot of personal attention given by your instructor</span></li>
    </ul>
  </section>

  <section class="abs paradise">
    <h2>Underwater <em>Paradise</em></h2>
    <div class="lead">
      <p>Bonaire is the place to learn how to scuba dive. After a brief introduction we will directly dive into the sea, where the reef starts in shallow waters. We know the perfect dive sites for beginners.</p>
      <p>Here, the sea bed slopes gradually down and you'll be amazed by the most beautiful fish and corals.</p>
    </div>
  </section>

  <p class="abs note">Stop by at our Front office and we are happy to answer all your questions or to book your 'Tidewalk Intro Dive'!</p>

  <p class="abs book-now">BOOK<br>NOW</p>
  <svg class="abs book-icon" width="30" height="30" viewBox="0 0 30 30" aria-hidden="true">
    <rect x="2" y="4" width="21" height="20" rx="1.5" fill="none" stroke="var(--orange)" stroke-width="1.6"/>
    <line x1="2" y1="10" x2="23" y2="10" stroke="var(--orange)" stroke-width="1.6"/>
    <line x1="7" y1="1.5" x2="7" y2="6" stroke="var(--orange)" stroke-width="1.6"/>
    <line x1="18" y1="1.5" x2="18" y2="6" stroke="var(--orange)" stroke-width="1.6"/>
    <circle cx="21.5" cy="22" r="6.5" fill="#fff" stroke="var(--orange)" stroke-width="1.6"/>
    <path d="M21.5 18.5v3.8h3" fill="none" stroke="var(--orange)" stroke-width="1.4"/>
  </svg>
  <div class="abs contact">
    <b>000 555 0190</b>
    <span>www.qmdivebonaire.example</span>
  </div>
</main>
</body>
</html>
```